Website Required for Small Cyber Security Company

Require a website for Cyber Security company. I have logo which i will attach. Please use logo blue and white as a guide
Would ultimately like the site to have a technology theme with the following pages Landing page
Services
Contact
Careers

I can provide content for each of those pages in due course, until then happy for you to use dummy data to display purposes

Target Market(s)

Government

Industry/Entity Type

Cyber Security

Coding

Coded - Design and coding required

Number of Pages Required

4 page

Colors
0054AA
0677BA
7BADD7
CADEEF
E8F1F8

Requirements
Must have
• High quality finish and UX
Nice to have
• look and feel professional and not cheap

```html
<!DOCTYPE html>
<html lang="en">
<head>
<meta charset="utf-8">
<title>Harlow Ridge Consulting</title>
<link rel="stylesheet" href="https://fonts.googleapis.com/css2?family=Poppins:wght@400;500;600&family=Lato:wght@400;700&display=swap">
<style>
:root{
  --blue-deep:#0054AA;
  --blue:#0677BA;
  --blue-mid:#7BADD7;
  --blue-light:#CADEEF;
  --blue-pale:#E8F1F8;
  --ink:#1d1d1f;
  --text:#333;
  --white:#fff;
  --black:#000;
}
*{box-sizing:border-box;margin:0;padding:0}
html,body{width:1200px;height:3000px;overflow:hidden;background:var(--white)}
body{font-family:'Lato',sans-serif;color:var(--text);position:relative}
.abs{position:absolute}
.heading{font-family:'Poppins',sans-serif}

/* header */
.topbar{left:414px;top:0;width:786px;height:56px;background:linear-gradient(90deg,var(--blue-deep),var(--blue));border-bottom-left-radius:40px;color:var(--white);font-family:'Lato',sans-serif;font-weight:700;font-size:17px;display:flex;align-items:center;padding-left:36px;gap:22px}
.topbar .sep{width:1px;height:20px;background:rgba(255,255,255,.7)}
.topbar .item{display:flex;align-items:center;gap:9px}
.social{display:flex;gap:9px}
.social span{width:28px;height:28px;border:1.5px solid var(--white);border-radius:50%}
.logo-plate{left:105px;top:-160px;width:255px;height:360px;background:var(--white);border-radius:50%;z-index:2}
.brand{z-index:3;display:flex;flex-direction:column;align-items:center}
.brand .mark{border-radius:50%;border:5px solid var(--blue)}
.brand .name{font-family:'Poppins',sans-serif;font-weight:600;color:var(--blue-deep);letter-spacing:.5px;white-space:nowrap}
.nav{top:96px;font-size:14px;color:#222;letter-spacing:.3px}
.nav.active{color:var(--blue);text-decoration:underline;font-weight:700}
.btn{background:var(--blue);color:var(--white);font-weight:700;font-size:13px;display:flex;align-items:center;justify-content:center;box-shadow:0 4px 8px rgba(0,0,0,.25)}

/* hero */
.hero{left:0;top:158px;width:1200px;height:646px}
.hero-title{left:117px;top:318px;color:var(--white);font-family:'Poppins',sans-serif;font-size:72px;line-height:86px}
.hero-title b{font-weight:600}
.hero-text{left:117px;top:496px;width:460px;color:var(--white);font-size:15px;line-height:26px}
.dot{top:751px;width:11px;height:11px;border-radius:50%;background:var(--white)}

/* services */
.section-title{width:1200px;left:0;text-align:center;font-family:'Poppins',sans-serif;font-weight:500;font-size:31px;color:var(--ink);letter-spacing:.5px}
.section-title span{color:var(--blue)}
.card{top:976px;width:306px;height:323px;background:var(--white);border-radius:34px 34px 4px 34px;box-shadow:0 2px 8px rgba(0,0,0,.08);text-align:center}
.card.lifted{border-radius:34px 4px 4px 34px;box-shadow:0 12px 18px rgba(0,0,0,.18)}
.card .icon{position:absolute;left:101px;top:30px;width:104px;height:104px;border-radius:50%;background:var(--blue-light);display:flex;align-items:center;justify-content:center}
.card.lifted .icon{background:var(--blue)}
.card h3{position:absolute;top:150px;width:100%;font-family:'Poppins',sans-serif;font-weight:500;font-size:24px;color:#222}
.card .bar{position:absolute;left:135px;top:184px;width:36px;height:4px;background:#8c8c8c}
.card.lifted .bar{background:var(--blue)}
.card p{position:absolute;top:213px;left:16px;width:274px;font-size:13.5px;line-height:26px;color:#333}
.arrow{top:1129px;width:38px;height:38px;border-radius:50%;display:flex;align-items:center;justify-content:center}

/* careers */
.careers{left:0;top:1404px;width:1200px;height:557px;background:linear-gradient(160deg,#0a6fae,#0b5d98 60%,#0a6aa8)}
.careers-title{left:646px;top:1510px;color:var(--white);font-family:'Poppins',sans-serif;font-weight:500;font-size:31px}
.careers-text{left:647px;top:1582px;width:436px;color:var(--white);font-size:15.5px;line-height:25.8px}

/* contact */
.addr-label{left:113px;top:2145px;font-family:'Lato',sans-serif;font-weight:700;font-size:22px;color:#111}
.c-icon{width:46px;height:46px;border-radius:50%;background:linear-gradient(135deg,var(--blue),var(--blue-mid));display:flex;align-items:center;justify-content:center}
.c-text{font-size:16px;line-height:26px;color:#111}
.field{background:var(--white);box-shadow:0 2px 6px rgba(0,0,0,.12);font-size:15px;color:#444;padding:16px 17px}

/* footer */
.footer-title{font-family:'Lato',sans-serif;font-weight:700;font-size:18px;color:var(--white);letter-spacing:.3px}
.footer-text{font-family:'Lato',sans-serif;font-size:16px;color:var(--white);line-height:26px}
.f-social{top:2823px;width:41px;height:41px;border-radius:50%;background:var(--white)}
</style>
</head>
<body>

<!-- header -->
<div class="abs topbar">
  <div class="item">
    <svg width="14" height="14" viewBox="0 0 24 24" fill="#fff"><path d="M6.6 10.8a15 15 0 0 0 6.6 6.6l2.2-2.2c.3-.3.7-.4 1-.2 1.1.4 2.3.6 3.6.6.6 0 1 .4 1 1V20c0 .6-.4 1-1 1A17 17 0 0 1 3 4c0-.6.4-1 1-1h3.5c.6 0 1 .4 1 1 0 1.3.2 2.5.6 3.6.1.3 0 .7-.2 1z"/></svg>
    +1 888 888 8888
  </div>
  <div class="sep"></div>
  <div class="item">
    <svg width="15" height="12" viewBox="0 0 24 18" fill="#fff"><path d="M0 0h24v3L12 10 0 3zM0 6l12 7 12-7v12H0z"/></svg>
    info@harlowridgeconsulting.com
  </div>
  <div class="sep"></div>
  <div class="social"><span></span><span></span><span></span><span></span></div>
</div>

<div class="abs logo-plate"></div>
<div class="abs brand" style="left:118px;top:6px;width:230px">
  <div class="mark" style="width:72px;height:72px"></div>
  <div class="name" style="font-size:24px;margin-top:10px">HARLOW RIDGE</div>
  <div class="name" style="font-size:11px;letter-spacing:4px;margin-top:-2px;color:var(--blue)">CONSULTING</div>
</div>

<div class="abs nav active" style="left:525px">HOME</div>
<div class="abs nav" style="left:617px">SERVICES</div>
<div class="abs nav" style="left:730px">CONTACT</div>
<div class="abs nav" style="left:845px">CAREERS</div>
<div class="abs btn" style="left:968px;top:86px;width:120px;height:42px">CONTACT US</div>

<!-- hero -->
<svg class="abs hero" viewBox="0 0 1200 646" role="img" aria-label="Cyber security themed photo of a hand touching a glowing digital interface">
  <defs>
    <linearGradient id="heroFill" x1="0" y1="0" x2="1" y2="1">
      <stop offset="0" stop-color="#07243b"/>
      <stop offset=".55" stop-color="#0b4a66"/>
      <stop offset="1" stop-color="#1b8aa6"/>
    </linearGradient>
    <linearGradient id="swoosh" x1="0" x2="1">
      <stop offset="0" stop-color="#0677BA"/>
      <stop offset=".6" stop-color="#0054AA"/>
      <stop offset="1" stop-color="#7BADD7"/>
    </linearGradient>
  </defs>
  <path d="M0 0H1200V520Q880 700 600 640Q280 640 0 520Z" fill="url(#heroFill)"/>
  <path d="M0 528Q300 650 620 640Q900 640 1200 520V536Q900 660 620 656Q300 660 0 548Z" fill="url(#swoosh)"/>
</svg>
<div class="abs hero-title"><b>Harlow Ridge</b><br>Consulting</div>
<div class="abs hero-text">Lorem ipsum dolor sit amet, consectetur adipiscing elit, sed do eiusmod tempor incididunt ut labore et dolore magna aliqua.</div>
<div class="abs btn" style="left:117px;top:577px;width:121px;height:43px">GET STARTED</div>
<div class="abs dot" style="left:573px"></div>
<div class="abs" style="left:588px;top:746px;width:21px;height:21px;border-radius:50%;background:var(--white);border:4px solid var(--white);box-shadow:inset 0 0 0 6px var(--blue)"></div>
<div class="abs dot" style="left:615px"></div>

<!-- services -->
<div class="abs section-title" style="top:888px">HARLOW RIDGE <span>SERVICES</span></div>

<div class="abs card" style="left:106px">
  <div class="icon"><svg width="52" height="52" viewBox="0 0 52 52" fill="none" stroke="#0677BA" stroke-width="2.5"><circle cx="22" cy="26" r="14"/><circle cx="22" cy="26" r="6"/><path d="M36 16h10M36 26h12M36 36h10"/><circle cx="47" cy="16" r="2"/><circle cx="48" cy="36" r="2"/></svg></div>
  <h3>Technology</h3><div class="bar"></div>
  <p>Lorem ipsum dolor sit amet, consectetur adipiscing elit, sed do eiusmod tempor incididunt ut labore et dolore magna aliqua.</p>
</div>
<div class="abs card lifted" style="left:445px">
  <div class="icon"><svg width="54" height="54" viewBox="0 0 54 54" fill="none" stroke="#fff" stroke-width="2.5"><path d="M27 5l18 7v13c0 12-8 20-18 24C17 45 9 37 9 25V12z"/><rect x="19" y="25" width="16" height="12" rx="2"/><path d="M22 25v-4a5 5 0 0 1 10 0v4"/></svg></div>
  <h3>Security</h3><div class="bar"></div>
  <p>Lorem ipsum dolor sit amet, consectetur adipiscing elit, sed do eiusmod tempor incididunt ut labore et dolore magna aliqua.</p>
</div>
<div class="abs card" style="left:782px">
  <div class="icon"><svg width="50" height="50" viewBox="0 0 50 50" fill="none" stroke="#0677BA" stroke-width="2.5"><circle cx="18" cy="28" r="9"/><circle cx="18" cy="28" r="3"/><path d="M30 10l10 10M40 10L30 20M30 40l14-14M38 26h6v6"/></svg></div>
  <h3>Strategy</h3><div class="bar"></div>
  <p>Lorem ipsum dolor sit amet, consectetur adipiscing elit, sed do eiusmod tempor incididunt ut labore et dolore magna aliqua.</p>
</div>
<div class="abs arrow" style="left:52px;background:#8a8a8a"><svg width="14" height="14" viewBox="0 0 14 14"><path d="M9 2L4 7l5 5" stroke="#fff" stroke-width="2.2" fill="none"/></svg></div>
<div class="abs arrow" style="left:1107px;background:var(--blue-deep)"><svg width="14" height="14" viewBox="0 0 14 14"><path d="M5 2l5 5-5 5" stroke="#fff" stroke-width="2.2" fill="none"/></svg></div>

<!-- careers -->
<div class="abs careers" role="img" aria-label="Blue digital circuitry and hexagon background"></div>
<svg class="abs" style="left:112px;top:1456px" width="430" height="450" viewBox="0 0 430 450">
  <path d="M215 4A221 221 0 1 0 416 350L390 336A190 190 0 1 1 390 114L416 100A221 221 0 0 0 215 4Z" fill="#fff"/>
</svg>
<div class="abs" role="img" aria-label="Photo of two IT specialists reviewing a tablet in a server monitoring room" style="left:144px;top:1489px;width:390px;height:385px;border-radius:50%;background:radial-gradient(circle at 40% 40%,#3d7fb8,#123a63 70%)"></div>
<div class="abs careers-title">OUR CAREERS</div>
<div class="abs careers-text">Lorem ipsum dolor sit amet, consectetur adipiscing elit, sed do eiusmod tempor incididunt ut labore et dolore magna aliqua. Ut enim ad minim veniam, quis nostrud exercitation ullamco laboris nisi ut aliquip ex ea commodo consequat. Duis aute irure dolor in reprehenderit in voluptate velit esse cillum dolore eu fugiat nulla pariatur. Excepteur sint occaecat cupidatat non proident, sunt in culpa qui officia deserunt mollit anim id est laborum.</div>
<div class="abs btn" style="left:647px;top:1800px;width:120px;height:43px;background:var(--white);color:var(--blue)">LEARN MORE</div>

<!-- contact -->
<div class="abs section-title" style="top:2046px">HARLOW RIDGE <span>CONTACT US</span></div>
<div class="abs addr-label">Address</div>

<div class="abs c-icon" style="left:111px;top:2190px"><svg width="16" height="20" viewBox="0 0 16 20" fill="#fff"><path d="M8 0a8 8 0 0 1 8 8c0 6-8 12-8 12S0 14 0 8a8 8 0 0 1 8-8zm0 5a3 3 0 1 0 0 6 3 3 0 0 0 0-6z"/></svg></div>
<div class="abs c-text" style="left:171px;top:2187px">Harlow Ridge Consulting<br>Addres here</div>
<div class="abs c-icon" style="left:111px;top:2267px"><svg width="18" height="18" viewBox="0 0 24 24" fill="#fff"><path d="M6.6 10.8a15 15 0 0 0 6.6 6.6l2.2-2.2c.3-.3.7-.4 1-.2 1.1.4 2.3.6 3.6.6.6 0 1 .4 1 1V20c0 .6-.4 1-1 1A17 17 0 0 1 3 4c0-.6.4-1 1-1h3.5c.6 0 1 .4 1 1 0 1.3.2 2.5.6 3.6.1.3 0 .7-.2 1z"/></svg></div>
<div class="abs c-text" style="left:169px;top:2277px">+1 888 888 8888</div>
<div class="abs c-icon" style="left:111px;top:2341px"><svg width="18" height="14" viewBox="0 0 24 18" fill="#fff"><path d="M0 0h24v3L12 10 0 3zM0 6l12 7 12-7v12H0z"/></svg></div>
<div class="abs c-text" style="left:175px;top:2351px">info@harlowridgeconsulting.com</div>

<div class="abs field" style="left:509px;top:2142px;width:283px;height:49px">First Name</div>
<div class="abs field" style="left:803px;top:2142px;width:283px;height:49px">Last Name</div>
<div class="abs field" style="left:509px;top:2205px;width:283px;height:49px">Your Phone</div>
<div class="abs field" style="left:803px;top:2205px;width:283px;height:49px">Your Email</div>
<div class="abs field" style="left:509px;top:2269px;width:577px;height:111px">Message</div>
<div class="abs btn" style="left:509px;top:2410px;width:111px;height:42px;background:var(--blue-deep)">SUBMIT</div>

<!-- footer -->
<svg class="abs" style="left:0;top:2540px" width="1200" height="460" viewBox="0 0 1200 460">
  <defs>
    <linearGradient id="footLine" x1="0" x2="1">
      <stop offset="0" stop-color="#0677BA"/>
      <stop offset=".5" stop-color="#0054AA"/>
      <stop offset="1" stop-color="#8a8a8a"/>
    </linearGradient>
  </defs>
  <path d="M0 148Q300 12 600 12Q900 12 1200 148V460H0Z" fill="url(#footLine)"/>
  <path d="M0 168Q300 20 600 20Q900 20 1200 158V460H0Z" fill="#000"/>
</svg>
<div class="abs brand" style="left:110px;top:2700px;width:236px">
  <div class="mark" style="width:82px;height:82px;border-color:var(--white)"></div>
  <div class="name" style="font-size:28px;margin-top:14px;color:var(--white)">HARLOW RIDGE</div>
  <div class="name" style="font-size:13px;letter-spacing:4px;color:var(--white)">CONSULTING</div>
</div>

<div class="abs footer-title" style="left:416px;top:2692px">QUICK LINKS</div>
<div class="abs footer-text" style="left:416px;top:2736px">Home<br>Services<br>Contact<br>Careers</div>

<div class="abs footer-title" style="left:567px;top:2692px">CONTACT US</div>
<svg class="abs" style="left:568px;top:2748px" width="16" height="20" viewBox="0 0 16 20" fill="#fff"><path d="M8 0a8 8 0 0 1 8 8c0 6-8 12-8 12S0 14 0 8a8 8 0 0 1 8-8zm0 5a3 3 0 1 0 0 6 3 3 0 0 0 0-6z"/></svg>
<div class="abs footer-text" style="left:599px;top:2744px">Lorem ipsum dolor sit amet,<br>consectetur adipiscing</div>
<svg class="abs" style="left:567px;top:2812px" width="18" height="18" viewBox="0 0 24 24" fill="#fff"><path d="M6.6 10.8a15 15 0 0 0 6.6 6.6l2.2-2.2c.3-.3.7-.4 1-.2 1.1.4 2.3.6 3.6.6.6 0 1 .4 1 1V20c0 .6-.4 1-1 1A17 17 0 0 1 3 4c0-.6.4-1 1-1h3.5c.6 0 1 .4 1 1 0 1.3.2 2.5.6 3.6.1.3 0 .7-.2 1z"/></svg>
<div class="abs footer-text" style="left:599px;top:2808px">+1 (888) 888 8888</div>
<svg class="abs" style="left:567px;top:2848px" width="18" height="14" viewBox="0 0 24 18" fill="#fff"><path d="M0 0h24v3L12 10 0 3zM0 6l12 7 12-7v12H0z"/></svg>
<div class="abs footer-text" style="left:599px;top:2842px">info@harlowridgeconsulting.com</div>

<div class="abs footer-title" style="left:860px;top:2692px">NEWSLETTER</div>
<div class="abs" style="left:860px;top:2744px;width:224px;height:40px;background:var(--white);border-radius:4px;font-size:15px;color:#777;padding:10px 14px">Enter email</div>
<div class="abs" style="left:1031px;top:2744px;width:53px;height:40px;background:var(--blue);border-radius:0 4px 4px 0;display:flex;align-items:center;justify-content:center"><svg width="16" height="12" viewBox="0 0 24 18" fill="#fff"><path d="M0 0h24v3L12 10 0 3zM0 6l12 7 12-7v12H0z"/></svg></div>
<div class="abs f-social" style="left:889px"></div>
<div class="abs f-social" style="left:940px"></div>
<div class="abs f-social" style="left:992px"></div>
<div class="abs f-social" style="left:1043px"></div>

<div class="abs" style="left:112px;top:2910px;width:976px;height:1px;background:#333"></div>
<div class="abs footer-text" style="left:0;top:2940px;width:1200px;text-align:center;font-size:15px">©Copyrights 2023 Harlow Ridge Consulting &nbsp;| &nbsp; All Rights Reserved</div>

</body>
</html>
```